Velora Trenn Brochure for Chemicals Products

We need a bifold A3 brochure for the exhibition.
you can visit our company website (www.veloratrenn.example) for more information about our company.
Company logo and color code attached.
The brochure should contain brief introduction of company, industries, product, and contact (address , telephone and email; pavel.k@veloratrenn.example)

Product Portfolio:
1. Intermediates
2. Plastics
3. Rubber
4. Additive
5. Fiber
Detail of each products portfolio are in the website. we would like to add product detail but you may help to design how to put it beautifully.

Target Market(s)

Our customers are factories in related industry.

Industry/Entity Type

Automotive, Paint, Electrical Appliance, Tyre and footwear, Textile, Animal Feed, Lubricant

Font styles to use
Sans Serif

Requirements
Must have
• Logo, Product Portfolio for different market.
Nice to have
• prefer curve design rather than rectangular

```html
<!DOCTYPE html>
<html lang="en">
<head>
<meta charset="utf-8">
<title>Velora Trenn – 2023 Profile Brochure</title>
<link href="https://fonts.googleapis.com/css2?family=Poppins:wght@400;500;600;700&display=swap" rel="stylesheet">
<style>
  :root {
    --bg: #c9c9cc;
    --blue: #2289d0;
    --blue-deep: #1d5fae;
    --lime: #8dc63f;
    --tick: #27a85a;
    --ink: #222428;
    --muted: #4a4d52;
    --white: #ffffff;
    --fold: #a9a9ad;
  }
  * { margin: 0; padding: 0; box-sizing: border-box; }
  html, body { width: 1010px; height: 1200px; overflow: hidden; }
  body { background: var(--bg); font-family: "Poppins", sans-serif; color: var(--ink); position: relative; }

  .spread { position: absolute; width: 692px; height: 488px; background: var(--white); overflow: hidden;
            box-shadow: 2px 3px 5px rgba(0,0,0,.25); }
  .spread--cover { left: 94px; top: 105px; }
  .spread--inside { left: 198px; top: 649px; }
  .fold { position: absolute; top: 0; bottom: 0; width: 1px; background: var(--fold); z-index: 6; }

  .photo { position: absolute; }
  .photo--round { border-radius: 50%; }

  /* logo */
  .brand { position: absolute; display: flex; align-items: center; gap: 4px; color: var(--blue);
           font-weight: 500; font-size: 11px; letter-spacing: .5px; white-space: nowrap; }
  .brand__dot { width: 14px; height: 14px; border-radius: 50%; border: 1.5px solid var(--blue); }
  .brand--mini { font-size: 3.5px; gap: 1px; letter-spacing: .2px; }
  .brand--mini .brand__dot { width: 5px; height: 5px; border-width: .6px; }

  /* cover spread */
  .back-panel { position: absolute; left: 6px; top: 0; width: 216px; height: 100%; background: var(--blue); }
  .photo--powder { left: 60px; top: -111px; width: 272px; height: 272px; border: 3px solid var(--white);
                   background: radial-gradient(circle at 60% 40%, #9fd6d6 0%, #7fb7c2 30%, #d9dcd8 60%, #b8946a 100%); z-index: 2; }
  .back-copy { position: absolute; left: 21px; top: 223px; width: 160px; color: var(--white); font-weight: 600; }
  .back-copy__lead { font-size: 7.6px; line-height: 9.4px; margin-bottom: 9px; }
  .back-copy__contact-title { font-size: 9px; font-weight: 700; margin-top: 22px; margin-bottom: 8px; }
  .back-copy__small { font-size: 6px; line-height: 7.6px; margin-bottom: 7.8px; }

  .photo--bands { left: 238px; top: 143px; width: 284px; height: 284px; border: 3px solid var(--blue);
                  background: radial-gradient(circle at 58% 42%, #f1b84b 0%, #e35aa0 18%, #52b6c9 32%, #f4f1ec 52%, #e9e3da 100%); z-index: 3; }
  .profile-band { position: absolute; left: 345px; top: 77px; width: 141px; height: 23px; background: var(--blue);
                  color: var(--white); font-weight: 600; font-size: 16px; line-height: 23px; padding-left: 19px; z-index: 4; }
  .photo--pellets { left: 467px; top: -2px; width: 246px; height: 246px;
                    background: radial-gradient(circle at 55% 55%, #e3b49f 0%, #8fd0e4 35%, #6cc4e0 70%, #a9dcec 100%); z-index: 1; }
  .cover-tagline { position: absolute; left: 541px; top: 351px; width: 135px; font-size: 9px; line-height: 10.5px;
                   font-weight: 600; color: var(--ink); }
  .spread--cover .brand--back { left: 238px; top: 443px; }
  .spread--cover .brand--front { left: 541px; top: 443px; }

  /* inside spread – about */
  .photo--lab { left: 0; top: 0; width: 346px; height: 170px;
                background: linear-gradient(135deg, #3a62b8 0%, #8fb0e4 45%, #c9daf3 65%, #5578c6 100%); }
  .about-title { position: absolute; left: 23px; top: 20px; color: var(--white); font-weight: 700; font-size: 14px; }
  .photo--yarn { left: 17px; top: 336px; width: 120px; height: 152px;
                 background: linear-gradient(160deg, #2d55a6 0%, #1c3d86 50%, #274f9c 100%); }
  .about-disc { position: absolute; left: -65px; top: 141px; width: 218px; height: 218px; border-radius: 50%;
                background: var(--blue); border: 3px solid var(--white); z-index: 2; }
  .about-disc__text { position: absolute; left: 22px; top: 190px; width: 107px; color: var(--white);
                      font-size: 5.6px; line-height: 7px; font-weight: 600; z-index: 3; }
  .about-intro { position: absolute; left: 167px; top: 189px; width: 172px; color: var(--blue);
                 font-size: 6.9px; line-height: 8.4px; font-weight: 600; }
  .industries-title { position: absolute; left: 167px; top: 238px; color: var(--tick); font-size: 7.6px; font-weight: 600; }
  .industries { position: absolute; left: 167px; top: 255px; list-style: none; }
  .industries li { display: flex; align-items: center; gap: 6px; height: 9.3px; font-size: 5.6px; font-weight: 600; color: var(--ink); }
  .industries svg { width: 6px; height: 6px; flex: none; }
  .spread--inside .brand--about { left: 317px; top: 476px; }

  /* inside spread – products */
  .products-title { position: absolute; left: 367px; top: 19px; color: var(--lime); font-weight: 700; font-size: 14px; }
  .products-lead { position: absolute; left: 465px; top: 23px; width: 210px; font-size: 5.2px; line-height: 6.4px; font-weight: 600; }
  .products-rule { position: absolute; left: 465px; top: 40px; width: 20px; height: 1.5px; background: var(--blue); }
  .products-panel { position: absolute; left: 519px; top: 78px; width: 144px; height: 308px; border-radius: 13px; background: var(--blue); }
  .product-photo { position: absolute; width: 88px; height: 88px; border-radius: 50%; z-index: 2; }
  .product-photo--chem { left: 367px; top: 47px; background: radial-gradient(circle at 40% 75%, #e8195e 0%, #c9c3c0 45%, #f2c21a 70%, #3aa88f 100%); }
  .product-photo--plastic { left: 501px; top: 47px; background: radial-gradient(circle at 55% 60%, #e3b49f 0%, #7ccbe3 45%, #a9dcec 100%); }
  .product-photo--rubber { left: 367px; top: 191px; background: radial-gradient(circle at 62% 40%, #f1b84b 0%, #e35aa0 22%, #52b6c9 38%, #f4f1ec 60%); }
  .product-photo--additive { left: 501px; top: 191px; background: radial-gradient(circle at 45% 65%, #dfe6e2 0%, #a6d3d3 35%, #b8946a 70%, #e9e9e9 100%); }
  .product-photo--fiber { left: 367px; top: 340px; background: radial-gradient(circle at 45% 45%, #4a6fc0 0%, #2a4f9e 50%, #1c3d86 100%); }
  .product-photo--custom { left: 501px; top: 340px; background: radial-gradient(circle at 55% 40%, #c9daf3 0%, #6f90d4 45%, #2f56b0 100%); }
  .product { position: absolute; width: 124px; }
  .product__name { font-size: 7.4px; font-weight: 600; color: var(--blue); margin-bottom: 3px; }
  .product__desc { font-size: 4.4px; line-height: 5.6px; color: var(--muted); }
  .product--on-blue .product__name, .product--on-blue .product__desc { color: var(--white); }
  .product--chem { left: 366px; top: 144px; }
  .product--plastic { left: 535px; top: 144px; width: 118px; }
  .product--rubber { left: 366px; top: 288px; }
  .product--additive { left: 535px; top: 288px; width: 110px; }
  .product--fiber { left: 366px; top: 435px; }
  .product--custom { left: 535px; top: 435px; width: 110px; }
  .spread--inside .brand--products { left: 661px; top: 476px; }
</style>
</head>
<body>

<!-- Outer spread: back cover and front cover -->
<section class="spread spread--cover">
  <div class="back-panel"></div>
  <div class="photo photo--round photo--powder" role="img" aria-label="Hand pouring turquoise powder from a jar into a white bowl"></div>

  <div class="back-copy">
    <p class="back-copy__lead">We Create Value In Chemicals<br>Distribution Network</p>
    <p class="back-copy__lead">We are deeply dedicated to the long-term growth and success of our partners and our people. We are dedicated to producing measured value and results.</p>
    <p class="back-copy__contact-title">CONTACT US:</p>
    <p class="back-copy__small">Get In Touch With Us<br>We look forward to serving you.</p>
    <p class="back-copy__small">Have Any Question?</p>
    <p class="back-copy__small">+66 2 555 0147</p>
    <p class="back-copy__small">88/4 Soi Ratchada 7, Din Daeng,<br>Bangkok 10400 Thailand</p>
  </div>

  <div class="photo photo--round photo--pellets" role="img" aria-label="Hand holding light blue plastic pellets"></div>
  <div class="profile-band">2023 Profile</div>
  <div class="photo photo--round photo--bands" role="img" aria-label="Ball of colourful rubber bands on a wooden table"></div>

  <p class="cover-tagline">Established since 2004, Velora Trenn is a specialties chemicals and polymer distribution company.</p>

  <div class="brand brand--back"><span class="brand__dot"></span>VELORA TRENN</div>
  <div class="brand brand--front"><span class="brand__dot"></span>VELORA TRENN</div>
  <div class="fold" style="left:345px"></div>
</section>

<!-- Inner spread: about us and products -->
<section class="spread spread--inside">
  <div class="photo photo--lab" role="img" aria-label="Blue laboratory glassware with a dropper releasing a drop"></div>
  <h2 class="about-title">ABOUT US</h2>
  <div class="photo photo--yarn" role="img" aria-label="Spools of blue yarn"></div>
  <div class="about-disc"></div>
  <p class="about-disc__text">Established since 2004, Velora Trenn is a specialties chemicals and polymer distribution company serving customers in various industries, including coating, adhesives, automotive, electrical appliances, construction, medicals, tyre and rubber, animal feed, and textiles. Our products range from chemical intermediates, engineering plastics, synthetics rubber, additives, fiber and our own tailored made products.</p>

  <p class="about-intro">At Velora Trenn, our dedicated team thrive on providing innovative solutions and unmatched service to customers.<br>Visit www.veloratrenn.example to learn more.</p>
  <h3 class="industries-title">Our Focused Industries</h3>
  <ul class="industries">
    <li><svg viewBox="0 0 10 10"><circle cx="5" cy="5" r="5" fill="#27a85a"/><path d="M2.6 5.2 4.3 6.8 7.4 3.6" stroke="#fff" stroke-width="1.4" fill="none"/></svg>Diversified Industries Served</li>
    <li><svg viewBox="0 0 10 10"><circle cx="5" cy="5" r="5" fill="#27a85a"/><path d="M2.6 5.2 4.3 6.8 7.4 3.6" stroke="#fff" stroke-width="1.4" fill="none"/></svg>Coating</li>
    <li><svg viewBox="0 0 10 10"><circle cx="5" cy="5" r="5" fill="#27a85a"/><path d="M2.6 5.2 4.3 6.8 7.4 3.6" stroke="#fff" stroke-width="1.4" fill="none"/></svg>Agricultural</li>
    <li><svg viewBox="0 0 10 10"><circle cx="5" cy="5" r="5" fill="#27a85a"/><path d="M2.6 5.2 4.3 6.8 7.4 3.6" stroke="#fff" stroke-width="1.4" fill="none"/></svg>Automotive</li>
    <li><svg viewBox="0 0 10 10"><circle cx="5" cy="5" r="5" fill="#27a85a"/><path d="M2.6 5.2 4.3 6.8 7.4 3.6" stroke="#fff" stroke-width="1.4" fill="none"/></svg>Electrical &amp; Electronic</li>
    <li><svg viewBox="0 0 10 10"><circle cx="5" cy="5" r="5" fill="#27a85a"/><path d="M2.6 5.2 4.3 6.8 7.4 3.6" stroke="#fff" stroke-width="1.4" fill="none"/></svg>Construction</li>
    <li><svg viewBox="0 0 10 10"><circle cx="5" cy="5" r="5" fill="#27a85a"/><path d="M2.6 5.2 4.3 6.8 7.4 3.6" stroke="#fff" stroke-width="1.4" fill="none"/></svg>Consumer Industrial Goods</li>
    <li><svg viewBox="0 0 10 10"><circle cx="5" cy="5" r="5" fill="#27a85a"/><path d="M2.6 5.2 4.3 6.8 7.4 3.6" stroke="#fff" stroke-width="1.4" fill="none"/></svg>Food &amp; Feeds</li>
    <li><svg viewBox="0 0 10 10"><circle cx="5" cy="5" r="5" fill="#27a85a"/><path d="M2.6 5.2 4.3 6.8 7.4 3.6" stroke="#fff" stroke-width="1.4" fill="none"/></svg>Health Care</li>
    <li><svg viewBox="0 0 10 10"><circle cx="5" cy="5" r="5" fill="#27a85a"/><path d="M2.6 5.2 4.3 6.8 7.4 3.6" stroke="#fff" stroke-width="1.4" fill="none"/></svg>Lubricants</li>
    <li><svg viewBox="0 0 10 10"><circle cx="5" cy="5" r="5" fill="#27a85a"/><path d="M2.6 5.2 4.3 6.8 7.4 3.6" stroke="#fff" stroke-width="1.4" fill="none"/></svg>Medical</li>
    <li><svg viewBox="0 0 10 10"><circle cx="5" cy="5" r="5" fill="#27a85a"/><path d="M2.6 5.2 4.3 6.8 7.4 3.6" stroke="#fff" stroke-width="1.4" fill="none"/></svg>Packaging</li>
    <li><svg viewBox="0 0 10 10"><circle cx="5" cy="5" r="5" fill="#27a85a"/><path d="M2.6 5.2 4.3 6.8 7.4 3.6" stroke="#fff" stroke-width="1.4" fill="none"/></svg>Textile and Footwear</li>
    <li><svg viewBox="0 0 10 10"><circle cx="5" cy="5" r="5" fill="#27a85a"/><path d="M2.6 5.2 4.3 6.8 7.4 3.6" stroke="#fff" stroke-width="1.4" fill="none"/></svg>Tire and Rubber</li>
  </ul>
  <div class="brand brand--mini brand--about"><span class="brand__dot"></span>VELORA TRENN</div>

  <div class="fold" style="left:346px"></div>

  <h2 class="products-title">PRODUCTS</h2>
  <p class="products-lead">From upstream to downstream, our portfolio covers various polymer related products including customs formulation solutions</p>
  <div class="products-rule"></div>
  <div class="products-panel"></div>

  <div class="product-photo product-photo--chem" role="img" aria-label="Open paint cans in pink, yellow and teal"></div>
  <div class="product-photo product-photo--plastic" role="img" aria-label="Hand holding light blue plastic pellets"></div>
  <div class="product-photo product-photo--rubber" role="img" aria-label="Ball of colourful rubber bands"></div>
  <div class="product-photo product-photo--additive" role="img" aria-label="Turquoise powder poured into a bowl"></div>
  <div class="product-photo product-photo--fiber" role="img" aria-label="Spools of blue yarn"></div>
  <div class="product-photo product-photo--custom" role="img" aria-label="Laboratory glassware with a dropper"></div>

  <div class="product product--chem">
    <h4 class="product__name">Chemicals</h4>
    <p class="product__desc">Our chemicals range from intermediates, monomer, and other products bringing synergy to our client. We offer products to coating resin, ink, adhesive, polyurethane, lubricants, polymer polymerization, textile auxiliaries, etc.</p>
  </div>
  <div class="product product--plastic product--on-blue">
    <h4 class="product__name">Plastics</h4>
    <p class="product__desc">We offer polymer and compound materials including short glass fiber, long glass fiber, mineral fillers, conductive, flame retardant, magnetic compound, carbon fiber, color compound and other customs compound.</p>
  </div>
  <div class="product product--rubber">
    <h4 class="product__name">Rubber</h4>
    <p class="product__desc">We supply synthetic rubber to major tire producers as well as rubber compounder and converter.</p>
  </div>
  <div class="product product--additive product--on-blue">
    <h4 class="product__name">Additives</h4>
    <p class="product__desc">We provide wide product range of additives for plastics compound, rubber compound, coating, modified starch and animal feed. We also offer additive masterbatch used for packaging industries.</p>
  </div>
  <div class="product product--fiber">
    <h4 class="product__name">Fibers</h4>
    <p class="product__desc">We offer specialties staple fiber and filament yarn for nonwoven, textile spinning, flooring, abrasives, tire cord, and protection fabric. The functionalized products such as antibacteria, flame retardant, biodegradable fiber are also available.</p>
  </div>
  <div class="product product--custom">
    <h4 class="product__name">Customs Formulation</h4>
    <p class="product__desc">With our expertise and collaboration with partners, we are also to make products and services exclusively for the clients.</p>
  </div>
  <div class="brand brand--mini brand--products"><span class="brand__dot"></span>VELORA TRENN</div>
</section>

</body>
</html>
```